Presentation Folder for Crest Holdings

We are a new property management / real estate company in Denver Colorado and are in need of new stationary design. Attached are our business card and logo deigns. We are looking for our stationary design. We need a presentation folder design that is Professional, exciting, and approachable. We do not have a preference on folder layout (pockets, style of folding) but will most likely be using a standard two pocket folder design (roughly 9x12) but feel free to experiment with and folder style as long as we can find a place to print them. We would also like to have a matching letterhead/page design
Below is standard size of folder from plume press
Full Bleed Size
20.87" x 16.68"
53 x 42.4 cm
6260 x 5004 pixels
Document Trim Size
20.75" x 16.56"
52.7 x 42.1 cm
6225 x 4969 pixels
Target Market(s)
We are attempting to target the top end of the real estate market in Denver Colorado. Are target market is investors in real estate.
Industry/Entity Type
Property Management
Font styles to use
Other font styles liked:
- Would like to keep font same to logo
Look and feel
Each slider illustrates characteristics of the customer's brand and the style your logo design should communicate.

```html
<!DOCTYPE html>
<html lang="en">
<head>
<meta charset="utf-8">
<title>Crest Holdings — Presentation Folder</title>
<link rel="stylesheet" href="https://fonts.googleapis.com/css2?family=Oswald:wght@500;600&family=Open+Sans:wght@400;600&display=swap">
<style>
  :root {
    --canvas: #ececec;
    --sky: #5aafcd;
    --paper: #ffffff;
    --charcoal: #4a4a4a;
    --ink: #3a3a3a;
    --muted: #6b6b6b;
  }
  * { box-sizing: border-box; margin: 0; padding: 0; }
  html, body { width: 1200px; height: 1000px; overflow: hidden; background: var(--canvas); }
  .folder-spread {
    position: absolute; left: 180px; top: 220px;
    width: 840px; height: 560px;
    box-shadow: 0 18px 40px rgba(0,0,0,.18);
  }
  .folder-art { position: absolute; inset: 0; display: block; }
  .brand-name {
    font-family: "Oswald", sans-serif; font-weight: 600;
    color: var(--sky); letter-spacing: .5px; text-transform: uppercase;
    display: flex; align-items: center; gap: 6px; line-height: 1;
  }
  .brand-mark { display: inline-block; border-radius: 50%; background: var(--sky); }
  .front-brand {
    position: absolute; right: 28px; top: 196px; text-align: right;
  }
  .front-brand .brand-name { font-size: 20px; justify-content: flex-end; }
  .front-brand .brand-mark { width: 14px; height: 14px; }
  .tagline {
    font-family: "Open Sans", sans-serif; font-size: 7.5px; color: var(--ink);
    margin-top: 3px; letter-spacing: .2px;
  }
  .back-contact {
    position: absolute; left: 282px; top: 440px;
    font-family: "Open Sans", sans-serif; color: var(--muted);
  }
  .back-contact .brand-name { font-size: 13px; margin-bottom: 4px; }
  .back-contact .brand-mark { width: 10px; height: 10px; }
  .contact-title { font-weight: 600; color: var(--sky); font-size: 7px; text-transform: uppercase; }
  .contact-line { font-size: 7px; line-height: 10px; display: flex; align-items: center; gap: 4px; }
  .contact-icon { width: 5px; height: 5px; background: var(--sky); border-radius: 1px; flex: none; }
  .contact-line.plain { padding-left: 0; }
</style>
</head>
<body>
  <div class="folder-spread">
    <svg class="folder-art" viewBox="0 0 840 560" aria-hidden="true">
      <defs>
        <clipPath id="front-panel"><rect x="420" y="0" width="420" height="560"/></clipPath>
      </defs>
      <!-- back cover -->
      <rect class="back-panel" x="0" y="0" width="420" height="560" fill="var(--sky)"/>
      <path class="back-sweep" d="M140 560 Q250 330 420 222 L420 560 Z" fill="var(--paper)"/>
      <!-- front cover -->
      <rect class="front-panel" x="420" y="0" width="420" height="560" fill="var(--paper)"/>
      <path class="front-sky" d="M420 0 H840 V180 Q620 148 420 222 Z" fill="var(--sky)"/>
      <circle class="front-disc" cx="810" cy="540" r="232" fill="var(--charcoal)" clip-path="url(#front-panel)"/>
      <line class="spine" x1="420" y1="0" x2="420" y2="560" stroke="rgba(0,0,0,.08)" stroke-width="1"/>
    </svg>

    <div class="front-brand">
      <div class="brand-name"><span class="brand-mark"></span>Crest Holdings</div>
      <div class="tagline">Property Management and Real Estate</div>
    </div>

    <div class="back-contact">
      <div class="brand-name"><span class="brand-mark"></span>Crest Holdings</div>
      <div class="contact-title">Crest Holdings</div>
      <div class="contact-line plain">P.O. Box 480216</div>
      <div class="contact-line plain">Denver, CO 80290</div>
      <div class="contact-line"><span class="contact-icon"></span>303 555 0142</div>
      <div class="contact-line"><span class="contact-icon"></span>(720) 555-0187</div>
      <div class="contact-line"><span class="contact-icon"></span>(720) 555-0163</div>
      <div class="contact-line"><span class="contact-icon"></span>info@crestholdingsco.com</div>
      <div class="contact-line"><span class="contact-icon"></span>www.crestholdingsco.com</div>
    </div>
  </div>
</body>
</html>
```